Modern Informational OBGYN website

Looking for a modern Wordpress website for a general OBGYN practice in Florida with a specialty in High Risk Obstetrics. We had an old Joomla website that crashed and we lost most of the files. It was over 10 years old and needed a refresh anyway.

Our practice serves a multicultural patient population (white, black, Spanish and Indian) and we would like our website to reflect that diversity. Our company colors are sunshine yellow (#ECBF6D) often combined with black, white and steel blue (#7191BE) in the "life" part of our logo (attached) depending on the background. Our tagline is "We're specialist in You!" Overall the site should have a clean modern yet comfortable feel. One that portrays friendliness and competence. At least 6 pages (Home, Obstetrics, Gynecology, News, Patient Education and Resources). Rotating stock pictures or videos are fine for the headers of the pages if the design you're considering calls for it. Interesting and creative use of typography and icons are encouraged.

The home page should have a call to action to schedule an appointment as well as a link to our patient portal. Other than the home and news pages, the other pages should have a similar look and feel. The home page should have sections on "About Us", "Medical Staff" (with pictures and brief bio for 2 male doctors, 2 female midwives and 1 female nurse practitioner), "Services" and "Location". The news page will be a closed blog that will not allow comments or responses. Both the obstetrics and the gynecology pages will have an educational blurb on the respective topics followed by a list of our services for each topic. Would be nice on the obstetrics page to have information and graphics changes that occur during each trimester (but not necessary). The resource page will have sections on at least "Office Forms", Office Policies", "OB Guide" each with multiple downloadable PDF's. Also a section on "Insurance" with a list of all the major insurance plans that we take with links to their company websites. The address, link and map to our hospital and their website can also go on this page. The Patient Education Page can be broken into 3 sections Obstetrics, Gynecology which both will have definition of medical disorders followed by FAQ's and "Helpful Links" which would have links to other website for medical information.

That's all that I can think of right now. The above is to help guide you but I am flexible, if the website design dictates a better flow of information. Looking forward to seeing what you can come up with. Down the road, I will be looking to the winning designer to produce matching brochures, full, half and quarter page media ads to have on hand for the practices further needs.

Target Market(s)

Women looking medical services

Industry/Entity Type

Medical

Coding

Coded - Design and coding required

Number of Pages Required

5+ page

Font styles to use
Sans Serif
Script

Colors

Designer to choose colors to be used in the design.

Requirements
Must have
• None. See projects description for suggestions
Nice to have
• infographics like information on stages of pregnancy on the obstetrics page

```html
<!DOCTYPE html>
<html lang="en">
<head>
<meta charset="utf-8">
<title>Heliacare OB/GYN Services</title>
<link href="https://fonts.googleapis.com/css2?family=Poppins:ital,wght@0,300;0,400;0,500;0,600;0,700;0,800;1,400&family=Playfair+Display:wght@400&display=swap" rel="stylesheet">
<style>
:root{
  --sun:#E9BC62;
  --sun-soft:#F3D9A4;
  --steel:#7191BE;
  --ink:#1d1d1d;
  --text:#6f6f6f;
  --light:#f3f3f3;
  --footer:#2a2a2a;
  --white:#ffffff;
}
*{margin:0;padding:0;box-sizing:border-box}
html,body{width:1200px;height:4528px;overflow:hidden;background:var(--white)}
body{position:relative;font-family:'Poppins',sans-serif;color:var(--ink)}
.abs{position:absolute}
a{color:inherit;text-decoration:none}

/* header */
.brand{position:absolute;left:88px;top:22px;display:flex;align-items:center;gap:10px}
.brand-dot{width:30px;height:30px;border-radius:50%;background:var(--sun)}
.brand-name{font-weight:700;font-size:26px;color:var(--ink);letter-spacing:1px;line-height:1}
.brand-sub{position:absolute;left:128px;top:56px;font-size:8px;letter-spacing:4px;font-weight:600;color:var(--ink)}
.nav{position:absolute;left:351px;top:32px;display:flex;gap:27px;font-size:12px;font-weight:500;text-transform:uppercase}
.nav .active{color:var(--sun)}
.btn-outline{position:absolute;left:922px;top:19px;width:188px;height:43px;border:2px solid var(--sun);display:flex;align-items:center;justify-content:center;font-size:11px;font-weight:600;text-transform:uppercase}

/* hero */
.hero-kicker{position:absolute;left:84px;top:254px;font-family:'Playfair Display',serif;font-size:72px;line-height:1;color:var(--ink)}
.hero-title{position:absolute;left:84px;top:328px;font-weight:800;font-size:76px;line-height:72px;letter-spacing:1px}
.hero-sub{position:absolute;left:90px;top:486px;font-size:17px;font-weight:500;text-transform:uppercase}
.btn-sun{position:absolute;background:var(--sun);color:var(--white);font-weight:600;text-transform:uppercase;display:flex;align-items:center;justify-content:center;letter-spacing:1px}
.hero-btn{left:88px;top:522px;width:237px;height:49px;font-size:13px}
.hero-ring{position:absolute;left:660px;top:235px;width:472px;height:472px;border-radius:50%;background:var(--sun-soft);opacity:.45}
.hero-photo{position:absolute;left:678px;top:253px;width:436px;height:436px;border-radius:50%;background:radial-gradient(circle at 55% 40%,#e9ecef 0 22%,#b6c98a 45%,#7e9e4a 100%)}

/* services */
.service{position:absolute;top:743px;width:260px;height:332px;border-radius:130px;background:var(--white);box-shadow:0 12px 34px rgba(0,0,0,.08);text-align:center}
.service-icon{width:94px;height:94px;border-radius:50%;margin:50px auto 0;display:flex;align-items:center;justify-content:center}
.service h3{margin-top:29px;font-size:15px;font-weight:600;text-transform:uppercase}
.service p{margin:18px auto 0;width:190px;font-size:13px;line-height:22px;color:var(--text)}

/* welcome */
.welcome-band{position:absolute;left:300px;top:1165px;width:815px;height:427px;border-radius:0 214px 214px 0;background:var(--sun)}
.welcome-photo{position:absolute;left:123px;top:1165px;width:440px;height:427px;border-radius:214px;background:linear-gradient(120deg,#d6e6c7,#a9c6a2 45%,#e8d6c6)}
.deco-lines{position:absolute;left:96px;top:1139px;width:136px;height:136px;border-radius:50%;background:#c9d6ea}
.deco-sun{position:absolute;left:126px;top:1495px;width:94px;height:94px;border-radius:50%;background:var(--sun)}
.welcome-kicker{position:absolute;left:617px;top:1262px;font-family:'Playfair Display',serif;font-size:18px;color:var(--white);letter-spacing:1px}
.welcome-title{position:absolute;left:615px;top:1286px;font-weight:700;font-size:36px;line-height:38px;color:var(--white)}
.welcome-text{position:absolute;left:617px;top:1364px;width:432px;font-size:14px;line-height:22px;color:var(--white)}
.btn-white{position:absolute;left:617px;top:1467px;width:154px;height:39px;background:var(--white);font-size:13px;font-weight:600;text-transform:uppercase;display:flex;align-items:center;justify-content:center}

/* care band */
.care-band{position:absolute;left:0;top:1706px;width:1200px;height:587px;background:linear-gradient(90deg,#efefef 0,#f4f4f4 40%,#e9e4e0 60%,#d9cfc8 100%)}
.care-title{position:absolute;left:163px;top:1910px;font-weight:700;font-size:36px;line-height:42px;text-transform:uppercase}
.care-text{position:absolute;left:165px;top:2040px;width:340px;font-size:14px;line-height:24px;color:var(--text)}

/* staff */
.section-title{position:absolute;left:0;width:1200px;text-align:center;font-weight:700;font-size:35px;text-transform:uppercase}
.rule{position:absolute;height:3px;background:var(--sun)}
.staff{position:absolute;top:2509px;width:246px;height:387px;border-radius:123px;background:var(--white);box-shadow:0 12px 34px rgba(0,0,0,.08);text-align:center}
.staff-photo{width:158px;height:158px;border-radius:50%;margin:30px auto 0;background:linear-gradient(180deg,#ececec,#d4d7dc)}
.staff h4{margin-top:20px;font-size:15px;font-weight:600;text-transform:uppercase}
.staff .role{margin-top:4px;font-size:10px;color:#9a9a9a;text-transform:uppercase;letter-spacing:.5px}
.staff p{margin:6px auto 0;width:205px;font-size:13px;line-height:21px;color:var(--text)}

/* testimonial */
.quote-mark{position:absolute;left:112px;top:3000px;font-family:'Playfair Display',serif;font-size:230px;line-height:1;color:#fbefd8}
.testi-title{position:absolute;left:123px;top:3100px;font-weight:700;font-size:34px;text-transform:uppercase}
.testi-text{position:absolute;left:123px;top:3180px;width:490px;font-style:italic;font-size:19px;line-height:30px;color:#555}
.testi-name{position:absolute;left:123px;top:3318px;font-size:14px;font-weight:600;color:var(--sun);text-transform:uppercase}
.testi-from{position:absolute;left:123px;top:3340px;font-size:12px;color:var(--ink)}
.dots{position:absolute;left:125px;top:3374px;display:flex;gap:16px}
.dots span{width:11px;height:11px;border-radius:50%;border:1px solid #ddd}
.dots .on{background:var(--sun);border-color:var(--sun)}
.testi-photo{position:absolute;left:643px;top:2998px;width:446px;height:446px;border-radius:50%;background:radial-gradient(circle at 50% 40%,#f2f3f5,#b9bcc0)}
.deco-stripe{position:absolute;left:975px;top:3026px;width:140px;height:140px;border-radius:50%;background:#c9d6ea;opacity:.8}
.deco-yellow{position:absolute;left:1019px;top:3066px;width:112px;height:112px;border-radius:50%;background:var(--sun);opacity:.7}
.deco-blue{position:absolute;left:656px;top:3319px;width:70px;height:70px;border-radius:50%;background:var(--steel);opacity:.7}

/* map */
.map{position:absolute;left:4px;top:3523px;width:1196px;height:530px;background:linear-gradient(135deg,#e6e6e6,#d8d8d8 50%,#cfcfcf)}
.map-card{position:absolute;left:111px;top:3625px;width:340px;height:340px;border-radius:50%;background:var(--white);box-shadow:0 10px 30px rgba(0,0,0,.1)}
.map-brand{position:absolute;left:184px;top:3680px;display:flex;align-items:center;gap:8px}
.map-brand .brand-dot{width:24px;height:24px}
.map-brand .brand-name{font-size:24px}
.map-sub{position:absolute;left:212px;top:3712px;font-size:8px;font-weight:600;letter-spacing:4px}
.map-info{position:absolute;left:152px;top:3766px}
.map-info h5{font-size:17px;font-weight:600;text-transform:uppercase;line-height:22px}
.map-info p{font-size:12px;color:#555;line-height:16px;margin-bottom:10px}

/* footer */
.footer{position:absolute;left:0;top:4053px;width:1200px;height:475px;background:var(--footer);color:var(--white)}
.foot-brand{position:absolute;left:137px;top:4252px;display:flex;align-items:center;gap:12px}
.foot-brand .brand-name{color:var(--white);font-size:38px}
.foot-brand .brand-dot{width:40px;height:40px}
.foot-sub{position:absolute;left:190px;top:4300px;font-size:11px;letter-spacing:6px;font-weight:600;color:var(--white)}
.foot-col{position:absolute;top:4183px;color:var(--white)}
.foot-col h6{font-size:16px;font-weight:600;text-transform:uppercase;margin-bottom:18px;color:var(--white)}
.foot-col li{list-style:none;font-size:12px;line-height:31px;color:#ddd;padding-left:4px}
.contact-row{display:flex;gap:10px;font-size:12px;line-height:18px;color:#ddd;margin-bottom:18px}
.foot-rule{position:absolute;left:94px;top:4466px;width:1012px;height:1px;background:#444}
.copyright{position:absolute;left:94px;top:4485px;font-size:12px;font-weight:500;color:var(--white);text-transform:uppercase}
.socials{position:absolute;left:955px;top:4484px;display:flex;gap:30px}
.socials span{width:15px;height:15px;border-radius:50%;background:var(--white)}
.to-top{position:absolute;left:1131px;top:4444px;width:42px;height:42px;border-radius:50%;background:var(--sun);display:flex;align-items:center;justify-content:center}
</style>
</head>
<body>

<!-- header -->
<div class="brand"><span class="brand-dot"></span><span class="brand-name">HELIACARE</span></div>
<div class="brand-sub">OB/GYN SERVICES</div>
<nav class="nav">
  <a class="active">Home</a><a>Obstetrics</a><a>Gynecology</a><a>News</a><a>Patient Education</a><a>Resources</a>
</nav>
<a class="btn-outline">Make an appointment</a>

<!-- hero -->
<div class="hero-kicker">WE'RE</div>
<h1 class="hero-title">SPECIALIST<br>IN YOU!</h1>
<p class="hero-sub">We work for your Heliacare OBGYN services</p>
<a class="btn-sun hero-btn">Make an appointment</a>
<div class="hero-ring"></div>
<div class="hero-photo" role="img" aria-label="Pregnant woman in white sitting on a sunny lawn"></div>

<!-- services -->
<div class="service" style="left:193px">
  <div class="service-icon" style="background:var(--sun)">
    <svg width="46" height="46" viewBox="0 0 46 46" fill="none" stroke="#fff" stroke-width="2.5"><circle cx="23" cy="23" r="17"/><circle cx="20" cy="19" r="5"/><path d="M14 30c4-5 13-5 18 0"/></svg>
  </div>
  <h3>Obstetrics</h3>
  <p>In a day and age like ours, good lifestyle practises are comprised we have.</p>
</div>
<div class="service" style="left:471px">
  <div class="service-icon" style="background:var(--steel)">
    <svg width="46" height="46" viewBox="0 0 46 46" fill="none" stroke="#fff" stroke-width="2.5"><rect x="8" y="8" width="30" height="22" rx="2"/><path d="M15 38h16M23 30v8M14 22l7-7 5 5 7-7"/></svg>
  </div>
  <h3>Patient Education</h3>
  <p>In a day and age like ours, good lifestyle practises are comprised we have.</p>
</div>
<div class="service" style="left:745px">
  <div class="service-icon" style="background:var(--sun)">
    <svg width="46" height="46" viewBox="0 0 46 46" fill="none" stroke="#fff" stroke-width="2.5"><circle cx="23" cy="17" r="9"/><path d="M23 26v14M17 34h12"/></svg>
  </div>
  <h3>Gynecology</h3>
  <p>In a day and age like ours, good lifestyle practises are comprised we have.</p>
</div>

<!-- welcome -->
<div class="welcome-band"></div>
<div class="deco-lines"></div>
<div class="welcome-photo" role="img" aria-label="Smiling expectant couple outdoors, man pointing into the distance"></div>
<div class="deco-sun"></div>
<div class="welcome-kicker">WELCOME TO</div>
<h2 class="welcome-title">HELIACARE OBGYN<br>SERVICES</h2>
<p class="welcome-text">Lorem ipsum dolor sit amet, consectetur adipis icing elit, sed do eius mod tempor incididunt ut labore et dolore magna aliqua. Ut enim ad min im veniam, quis nostrud exercitation ullamco laboris nisi ut aliquip ex tempore</p>
<a class="btn-white">Find out more</a>

<!-- care band -->
<div class="care-band" role="img" aria-label="Happy couple embracing while looking at a pregnancy test"></div>
<h2 class="care-title">Taking care<br>of you &amp; your<br>baby</h2>
<p class="care-text">We are award winning architects and we love exotic vehicles. Solace Bay combines our two passions:</p>

<!-- staff -->
<h2 class="section-title" style="top:2412px">Medical staff</h2>
<div class="rule" style="left:578px;top:2468px;width:44px"></div>

<div class="staff" style="left:88px"><div class="staff-photo" role="img" aria-label="Portrait of a female optometrist in white coat"></div><h4>Nora Ellison</h4><div class="role">Optometrist</div><p>Aenean a quam nec quam euismod pellentesque sodales tristique vestibulum...</p></div>
<div class="staff" style="left:348px"><div class="staff-photo" role="img" aria-label="Portrait of a male specialist in white coat"></div><h4>Marcus Delane</h4><div class="role">Specialist</div><p>Aenean a quam nec quam euismod pellentesque sodales tristique vestibulum...</p></div>
<div class="staff" style="left:606px"><div class="staff-photo" role="img" aria-label="Portrait of a female optometrist in white coat"></div><h4>Priya Ranwal</h4><div class="role">Optometrist</div><p>Aenean a quam nec quam euismod pellentesque sodales tristique vestibulum...</p></div>
<div class="staff" style="left:866px"><div class="staff-photo" role="img" aria-label="Portrait of a male specialist with glasses in white coat"></div><h4>Tomas Reyer</h4><div class="role">Specialist</div><p>Aenean a quam nec quam euismod pellentesque sodales tristique vestibulum...</p></div>

<!-- testimonial -->
<div class="quote-mark">&ldquo;</div>
<h2 class="testi-title">What our client say</h2>
<div class="rule" style="left:123px;top:3158px;width:44px;height:2px;background:#ddd"></div>
<p class="testi-text">Aenean sollicitudin, lorem quis bibendum auctor, nisi elit consequat ipsum, nec sagittis sem nibh id elit duis sed odio sit amet nibh vulputate cursus a sit amet mauris. Morbi accumsan ipsum velit.</p>
<div class="testi-name">-Lena Okafor</div>
<div class="testi-from">from Tampa, FL</div>
<div class="dots"><span class="on"></span><span></span><span></span></div>
<div class="testi-photo" role="img" aria-label="Smiling pregnant woman in a white shirt holding her belly"></div>
<div class="deco-stripe"></div>
<div class="deco-yellow"></div>
<div class="deco-blue"></div>

<!-- location -->
<div class="map" role="img" aria-label="Street map around the clinic location"></div>
<svg class="abs" style="left:764px;top:3722px" width="26" height="34" viewBox="0 0 26 34"><path d="M13 0C6 0 0 6 0 13c0 9 13 21 13 21s13-12 13-21C26 6 20 0 13 0z" fill="var(--sun)"/><circle cx="13" cy="13" r="5" fill="#fff"/></svg>
<div class="map-card"></div>
<div class="map-brand"><span class="brand-dot"></span><span class="brand-name">HELIACARE</span></div>
<div class="map-sub">OB/GYN SERVICES</div>
<div class="map-info">
  <h5>Call + 555 0142 880</h5><p>Some address line, Bayview FL 33</p>
  <h5>Open hours</h5><p>Mon-Sat: 8am - 5pm, Sun: Closed</p>
  <h5>Make an appointment</h5><p>It's Spo Fast and Easy</p>
</div>

<!-- footer -->
<footer class="footer"></footer>
<div class="foot-brand"><span class="brand-dot"></span><span class="brand-name">HELIACARE</span></div>
<div class="foot-sub">OB/GYN SERVICES</div>
<div class="foot-col" style="left:466px"><h6>Quick links</h6><ul><li>Home</li><li>Obstetrics</li><li>Gynecology</li><li>News</li><li>Patient Education</li><li>Resources</li></ul></div>
<div class="foot-col" style="left:662px"><h6>Information</h6><ul><li>Privacy Policy</li><li>Terms &amp; Conditions</li><li>Shipping Policy</li><li>FAQ's</li><li>Sitemap</li><li>Blog</li></ul></div>
<div class="foot-col" style="left:873px"><h6>Contact info</h6>
  <div class="contact-row"><svg width="13" height="13" viewBox="0 0 13 13"><rect x="0" y="2" width="13" height="9" fill="var(--sun)"/><path d="M0 2l6.5 5L13 2" stroke="#2a2a2a" fill="none"/></svg><div>Email:<br>hello@heliacare-demo.com</div></div>
  <div class="contact-row"><svg width="13" height="13" viewBox="0 0 24 24"><path d="M6 2l4 5-2 3c1 3 3 5 6 6l3-2 5 4-3 4C10 22 2 14 2 5z" fill="var(--sun)"/></svg><div>Phone:<br>+1 555 014 2880</div></div>
  <div class="contact-row"><svg width="13" height="16" viewBox="0 0 26 34"><path d="M13 0C6 0 0 6 0 13c0 9 13 21 13 21s13-12 13-21C26 6 20 0 13 0z" fill="var(--sun)"/></svg><div>Location:<br>Some address line goes<br>here city name</div></div>
</div>
<div class="foot-rule"></div>
<div class="copyright">&copy; Copyright 2022 Heliacare all rights reserved</div>
<div class="socials"><span></span><span></span><span></span><span></span></div>
<div class="to-top"><svg width="14" height="16" viewBox="0 0 14 16" fill="none" stroke="#fff" stroke-width="2"><path d="M7 15V2M2 7l5-5 5 5"/></svg></div>

</body>
</html>
```